Reed diffusers - packing design

Dear Sir/Madam,

For this project, we would like to come up with a different style of product packing design for our reed diffuser Mandarin 100ml.

Important:

The text on the box should remain the same, the logo should be positioned on the same location and it is very important to keep the text ‘’Reed diffuser’’ and the type of fragrance on the front of the packing.

This are the key and main keywords for the positions, and the customer must identify the product and relate to fragrance.
Besides that, we can think of any kind of graphic design style.

We are trying to advertise/sell a smell/scent
It brings you back to a place/memory/experience and can be displayed/visualized in form of an image or icon (natural/organic) in order to express a feeling or an emotion which a potential customer can relate

We follow the strategy of applying matching colors (for the scent variations) on the main page and we want to identify colors which are not used by competitors (USP)

The packaging itself should be perceived as a gift box and should have a luxury touch
On the package itself - it should be included a hint of the most common locations which are likely used for a “Reed Diffuser” (Comfort room, Living room) associated in form of a pattern or icons.

Font: Adobe Garamond Pro en Arial

With kind regards,

```html
<!DOCTYPE html>
<html lang="en">
<head>
<meta charset="utf-8">
<title>Citrelle Reed Diffuser Mandarin – Packaging</title>
<link rel="stylesheet" href="https://fonts.googleapis.com/css2?family=Cabin:wght@500&family=Nunito:wght@400;600;900&family=Roboto+Condensed:wght@400&display=swap">
<style>
  :root {
    --page: #f1f1f1;
    --orange-deep: #ef6a0a;
    --orange: #f7841c;
    --orange-light: #fba23a;
    --apricot: #fdc060;
    --bubble: #ffd25a;
    --white: #ffffff;
    --ink: #2a1a10;
    --hazard-red: #d9241c;
  }
  * { margin: 0; padding: 0; box-sizing: border-box; }
  html, body { width: 845px; height: 1200px; overflow: hidden; background: var(--page); }
  .canvas { position: relative; width: 845px; height: 1200px; }

  .panel { position: absolute; top: 100px; height: 1000px; overflow: hidden; }
  .panel-side { left: 150px; width: 170px; background: var(--orange); }
  .panel-front { left: 320px; width: 370px; background: var(--white); }
  .panel-bg { position: absolute; inset: 0; width: 100%; height: 100%; }

  .side-copy {
    position: absolute; left: 14px; right: 14px;
    font-family: "Roboto Condensed", sans-serif; font-size: 11.5px; line-height: 1.3;
    color: var(--ink); text-align: center;
  }
  .side-copy-top { top: 60px; }
  .side-copy-bottom { top: 600px; font-size: 10.5px; }
  .hazards { position: absolute; left: 10px; bottom: 40px; width: 150px; height: 150px; }

  .brand { position: absolute; top: 60px; left: 0; width: 100%; text-align: center; z-index: 1; }
  .brand-mark { width: 120px; height: 120px; margin: 0 auto; border: 3px solid var(--white); border-radius: 50%; }
  .brand-name {
    margin-top: 16px; font-family: "Cabin", sans-serif; font-weight: 500; font-size: 28px;
    letter-spacing: 0.5px; color: var(--white);
  }
  .product-title {
    position: absolute; top: 300px; left: 0; width: 100%; text-align: center; z-index: 1;
    color: var(--white); font-family: "Nunito", sans-serif; font-weight: 900;
  }
  .product-type { font-size: 31px; letter-spacing: 0.5px; line-height: 1; }
  .product-scent { font-size: 47px; letter-spacing: 0.5px; line-height: 1.15; }

  .diffuser-art {
    position: absolute; left: 115px; top: 470px; width: 140px; height: 340px;
    background: linear-gradient(180deg, #c9b8a8 0%, #b9aca3 55%, #8f8a88 80%, #5a3a50 100%);
    opacity: 0.85; border-radius: 6px;
  }

  .tagline {
    position: absolute; top: 845px; left: 0; width: 100%; text-align: center;
    font-family: "Nunito", sans-serif; font-size: 17px; line-height: 1.1; color: var(--orange-deep);
  }
  .use-label {
    position: absolute; top: 905px; left: 0; width: 100%; text-align: center;
    font-family: "Nunito", sans-serif; font-size: 13px; letter-spacing: 0.5px; color: var(--orange-deep);
  }
  .rooms { position: absolute; top: 925px; left: 0; width: 100%; display: flex; justify-content: center; align-items: center; gap: 8px; }
  .room {
    width: 62px; height: 62px; border-radius: 50%; background: var(--orange-deep); color: var(--white);
    display: flex; align-items: flex-end; justify-content: center; padding-bottom: 12px;
    font-family: "Nunito", sans-serif; font-size: 8px; font-weight: 600;
  }
  .room-divider { width: 1px; height: 40px; background: var(--orange-deep); }
</style>
</head>
<body>
<main class="canvas">

  <section class="panel panel-side">
    <svg class="panel-bg" viewBox="0 0 170 1000" preserveAspectRatio="none" aria-hidden="true">
      <rect width="170" height="1000" fill="#e8650c"/>
      <path d="M0 660 C60 600 120 560 170 520 L170 1000 L0 1000 Z" fill="#f58a22"/>
      <path d="M0 780 C70 720 130 700 170 690 L170 1000 L0 1000 Z" fill="#fbb24a"/>
      <path d="M0 900 C70 870 120 860 170 850 L170 1000 L0 1000 Z" fill="#ffffff"/>
      <path d="M20 620 C60 560 110 520 170 470" stroke="#ffffff" stroke-width="10" fill="none"/>
    </svg>
    <p class="side-copy side-copy-top">Lorem ipsum dolor sit amet, consectetur adipiscing elit, sed do eiusmod tempor incididunt ut labore et dolore magna aliqua. Ut enim ad minim veniam, quis nostrud exercitation ullamco laboris nisi ut aliquip ex ea commodo consequat. Duis aute irure dolor in reprehenderit in voluptate velit esse cillum dolore eu fugiat nulla pariatur. Excepteur sint occaecat cupidatat non proident, sunt in culpa qui officia deserunt mollit anim id est laborum.</p>
    <p class="side-copy side-copy-bottom">Lorem ipsum dolor sit amet, consectetur adipiscing elit, sed do eiusmod tempor incididunt ut labore et dolore magna aliqua. Ut enim ad minim veniam, quis nostrud exercitation ullamco laboris nisi ut aliquip ex ea commodo consequat. Duis aute irure dolor in reprehenderit in voluptate velit esse cillum dolore eu fugiat nulla pariatur. Excepteur sint occaecat cupidatat non proident, sunt in culpa qui officia deserunt mollit anim id est laborum.</p>
    <svg class="hazards" viewBox="0 0 150 150" aria-label="Safety warning symbols">
      <g fill="#ffffff" stroke="#d9241c" stroke-width="4">
        <rect x="18" y="18" width="40" height="40" transform="rotate(45 38 38)"/>
        <rect x="80" y="30" width="40" height="40" transform="rotate(45 100 50)"/>
        <rect x="45" y="85" width="40" height="40" transform="rotate(45 65 105)"/>
      </g>
    </svg>
  </section>

  <section class="panel panel-front">
    <svg class="panel-bg" viewBox="0 0 370 1000" preserveAspectRatio="none" aria-hidden="true">
      <defs>
        <linearGradient id="front-top" x1="0" y1="0" x2="0" y2="1">
          <stop offset="0" stop-color="#fba23a"/>
          <stop offset="0.6" stop-color="#f7841c"/>
        </linearGradient>
      </defs>
      <rect width="370" height="1000" fill="url(#front-top)"/>
      <path d="M370 290 C345 330 330 380 300 410 C260 450 220 470 180 520 C140 570 80 590 0 610 L0 1000 L370 1000 Z" fill="#f57410"/>
      <path d="M370 570 C300 590 250 640 215 710 C180 780 100 810 0 830 L0 1000 L370 1000 Z" fill="#fdc060"/>
      <path d="M370 620 C310 640 270 690 240 760 C210 820 140 840 0 860 L0 1000 L370 1000 Z" fill="#ffffff"/>
      <path d="M370 290 C345 330 330 380 300 410 C260 450 220 470 180 520 C140 570 80 590 0 610" stroke="#ffffff" stroke-width="14" fill="none"/>
      <g fill="none" stroke="#ffd25a" stroke-width="2.5">
        <circle cx="330" cy="50" r="13"/>
        <circle cx="40" cy="200" r="22"/>
        <circle cx="330" cy="250" r="13"/>
        <circle cx="290" cy="480" r="30"/>
      </g>
      <g fill="none" stroke="#f57410" stroke-width="2.5">
        <circle cx="320" cy="760" r="18"/>
        <circle cx="40" cy="810" r="16"/>
        <circle cx="320" cy="880" r="14"/>
      </g>
    </svg>

    <header class="brand">
      <div class="brand-mark"></div>
      <p class="brand-name">CITRELLE</p>
    </header>

    <h1 class="product-title">
      <span class="product-type">REED DIFFUSER</span><br>
      <span class="product-scent">MANDARIN</span>
    </h1>

    <div class="diffuser-art" role="img" aria-label="Illustration of a glass reed diffuser bottle with a dark cap and reed sticks"></div>

    <p class="tagline">with natural mandarin<br>essential oil</p>
    <p class="use-label">FOR USE IN</p>
    <div class="rooms">
      <div class="room" role="img" aria-label="Living room icon">LIVINGROOM</div>
      <span class="room-divider"></span>
      <div class="room" role="img" aria-label="Bathroom icon">BATHROOM</div>
      <span class="room-divider"></span>
      <div class="room" role="img" aria-label="Toilet icon">TOILET</div>
    </div>
  </section>

</main>
</body>
</html>
```